Food Hall in Marisol Bay, CA by the Pacific Ocean that has 15 vendors and 2 bars

We need a web page design that highlights our food hall in Marisol Bay, CA. The name of the food hall is Bellwick Food Hall. Inside of the food hall there are 15 different vendors and 2 bars. The place has a beautiful patio and it is by Pacific Ocean. Most of the vendors are local to Marisol Bay area. The highly anticipated location is opening during the summer of 2025. Website should have a dropdown menu for the different vendors that are in the food hall and people should be able to click to their respective business website. The website should also include link to our social media channels and also a link to provide comments and subscribe for the mailing list.
Target Market(s)
Mostly residents in the Marisol Bay, CA and surrounding areas. Couples, families and tourist alike that are looking for an exceptional dining experience that everyone can find something they like.
Industry/Entity Type
Restaurants
Coding
Coded - Design and coding required
Number of Pages Required
5+ page
Font styles to use
Look and feel

```html
<!DOCTYPE html>
<html lang="en">
<head>
<meta charset="UTF-8">
<title>Bellwick Food Hall</title>
<link rel="stylesheet" href="https://fonts.googleapis.com/css2?family=Lato:wght@400;700;900&display=swap">
<style>
  :root {
    --header-blue: #0390d2;
    --page-blue: #0152aa;
    --card-white: #ffffff;
    --heading-navy: #0d4f9c;
    --field-border: #7fa3d1;
    --placeholder: #555b63;
    --hero-sky: #6fc4ea;
    --hero-sea: #1fa5c4;
    --hero-sand: #ece6dc;
    --white: #ffffff;
  }
  * { box-sizing: border-box; margin: 0; padding: 0; }
  html, body {
    width: 1200px;
    height: 651px;
    overflow: hidden;
    font-family: 'Lato', sans-serif;
    background: var(--page-blue);
  }
  body { position: relative; }
  .site-header {
    height: 50px;
    background: var(--header-blue);
    display: flex;
    align-items: center;
    justify-content: space-between;
    padding: 0 0 0 11px;
  }
  .brand {
    color: var(--white);
    font-size: 21px;
    font-weight: 700;
    letter-spacing: 0.1px;
  }
  .main-nav {
    display: flex;
    height: 100%;
  }
  .main-nav a {
    width: 97px;
    display: flex;
    align-items: center;
    justify-content: center;
    color: var(--white);
    font-size: 11.5px;
    font-weight: 700;
    text-decoration: none;
  }
  .hero {
    position: relative;
    height: 298px;
    display: flex;
    flex-direction: column;
    align-items: center;
    color: var(--white);
    text-align: center;
  }
  .hero-photo {
    position: absolute;
    inset: 0;
    background: linear-gradient(180deg, var(--hero-sky) 0%, #8fd0ee 38%, #3aa6bf 56%, var(--hero-sea) 72%, #d9e8e6 80%, var(--hero-sand) 100%);
  }
  .hero-title {
    position: relative;
    margin-top: 115px;
    font-size: 32px;
    font-weight: 700;
    text-shadow: 0 1px 3px rgba(0,0,0,0.35);
  }
  .hero-tagline {
    position: relative;
    margin-top: 17px;
    font-size: 15.5px;
    font-weight: 400;
    text-shadow: 0 1px 2px rgba(0,0,0,0.35);
  }
  .signup-card {
    position: absolute;
    left: 224px;
    top: 369px;
    width: 753px;
    height: 282px;
    background: var(--card-white);
    border-radius: 8px 8px 0 0;
    padding: 0 22px;
    overflow: hidden;
  }
  .signup-title {
    margin-top: 48px;
    text-align: center;
    color: var(--heading-navy);
    font-size: 16.5px;
    font-weight: 700;
  }
  .field {
    display: block;
    width: 100%;
    border: 2px solid var(--field-border);
    border-radius: 5px;
    font-family: 'Lato', sans-serif;
    font-size: 10px;
    color: var(--placeholder);
    padding: 0 11px;
    background: var(--white);
  }
  .field-email {
    margin-top: 12px;
    height: 38px;
    line-height: 34px;
  }
  .field-comment {
    margin-top: 17px;
    height: 140px;
    padding-top: 10px;
  }
</style>
</head>
<body>
  <header class="site-header">
    <div class="brand">Bellwick Food Hall</div>
    <nav class="main-nav">
      <a href="#">Home</a>
      <a href="#">Vendors</a>
      <a href="#">About</a>
      <a href="#">Contact</a>
    </nav>
  </header>

  <section class="hero">
    <div class="hero-photo" role="img" aria-label="Sunny beach with palm tree, thatched umbrella, sailboat and green hills across the ocean"></div>
    <h1 class="hero-title">Welcome to Bellwick Food Hall</h1>
    <p class="hero-tagline">Opening Summer 2025 - Located on the beautiful terrace by the Pacific Ocean in Marisol Bay</p>
  </section>

  <section class="signup-card">
    <h2 class="signup-title">Stay in Touch</h2>
    <div class="field field-email">Enter your email</div>
    <div class="field field-comment">Leave a comment...</div>
  </section>
</body>
</html>
```